Ruby Deck Fun Casino Entertainment

Looking to update my business card and make it look more modern, stand out and eye catching.
We are are fun casino business in Australia (primarily Sydney). Blackjack and Roulette are our most popular games although we have pretty much every game available for hire that you would find in a real casino. The final design would need to be sleek and appeal to the more upmarket corporate sector.
We mainly cater for Corporate Events, Private Parties, Fundraising Events, Team Building, Poker Tournaments
I think I'd prefer the colour Black.

Target Market(s)

High-end Corporate

Industry/Entity Type

Events

Contact Information for Business Card

Ned Paxley
Director
1300 472 861
0438 705 705
info@rubydeckfun.com.au
www.rubydeckfun.com.au
Facebook & Instagram @rubydeckshowhire (proper social icons preferred)

Colors
000000
0255a3

Requirements
Must have
• Front side:
• Logo
• Contact details
• 'Australia's #1 Fun Casino Specialists'
• Back:
• Logo
Nice to have
• Back:
• Corporate Events
• Private Parties
• Poker Tournaments
• Fundraising
• Props & Theming
• Photo Booth
• Horse Racing Events
• The Vegas Sign attached, maybe on the back of the card in the background...?

```html
<!DOCTYPE html>
<html lang="en">
<head>
<meta charset="utf-8">
<title>Ruby Deck Fun Casino Entertainment – Business Card</title>
<link rel="stylesheet" href="https://fonts.googleapis.com/css2?family=Libre+Baskerville:wght@700&family=Open+Sans:wght@400;700&display=swap">
<style>
  :root {
    --page-bg: #2a2c30;
    --card-black: #050505;
    --ink-white: #f4f4f4;
    --ink-grey: #d8d8d8;
    --brand-gold: #f6a31c;
    --brand-gold-faint: #5e4a2c;
    --bokeh-dark: #120d0a;
    --bokeh-brown: #5a4634;
    --bokeh-warm: #8d7558;
  }
  * { box-sizing: border-box; margin: 0; padding: 0; }
  html, body {
    width: 1200px;
    height: 900px;
    overflow: hidden;
    background: var(--page-bg);
  }
  .canvas {
    width: 1200px;
    height: 900px;
    display: flex;
    align-items: center;
    justify-content: center;
    gap: 40px;
  }
  .card {
    position: relative;
    width: 525px;
    height: 300px;
    border-radius: 4px;
    overflow: hidden;
    box-shadow: 0 14px 30px rgba(0,0,0,0.5);
  }

  /* Contact side */
  .card-contact {
    background: var(--card-black);
    font-family: "Open Sans", sans-serif;
    color: var(--ink-white);
  }
  .contact-block {
    position: absolute;
    top: 22px;
    left: 30px;
    z-index: 1;
  }
  .person-name {
    font-family: "Libre Baskerville", serif;
    font-weight: 700;
    font-size: 22px;
    line-height: 30px;
    letter-spacing: 0.2px;
  }
  .person-title {
    font-size: 12px;
    letter-spacing: 0.8px;
    text-transform: uppercase;
    color: var(--ink-grey);
    padding-bottom: 6px;
    border-bottom: 1px solid var(--ink-grey);
    width: 82px;
    margin-bottom: 10px;
  }
  .contact-list { list-style: none; }
  .contact-item {
    display: flex;
    align-items: center;
    gap: 8px;
    font-size: 13px;
    line-height: 20px;
    white-space: nowrap;
  }
  .contact-icon {
    width: 13px;
    height: 13px;
    flex: none;
  }
  .contact-icon-pair { display: flex; gap: 3px; }
  .brand-faint {
    position: absolute;
    right: 24px;
    bottom: 22px;
    display: flex;
    align-items: center;
    gap: 12px;
  }
  .brand-faint-circle {
    width: 84px;
    height: 84px;
    border-radius: 50%;
    background: #141414;
    flex: none;
  }
  .brand-faint-name {
    font-family: "Open Sans", sans-serif;
    font-weight: 700;
    font-size: 26px;
    line-height: 1.1;
    text-transform: uppercase;
    color: var(--brand-gold-faint);
    white-space: nowrap;
  }

  /* Logo side */
  .card-logo {
    display: flex;
    align-items: center;
    justify-content: center;
  }
  .bokeh-backdrop {
    position: absolute;
    inset: 0;
    background:
      radial-gradient(ellipse at 30% 65%, var(--bokeh-warm) 0%, transparent 45%),
      radial-gradient(ellipse at 75% 80%, var(--bokeh-brown) 0%, transparent 40%),
      linear-gradient(180deg, var(--bokeh-dark) 0%, var(--bokeh-brown) 60%, var(--bokeh-dark) 100%);
  }
  .brand-mark {
    position: relative;
    display: flex;
    align-items: center;
    gap: 14px;
  }
  .brand-circle {
    width: 70px;
    height: 70px;
    border-radius: 50%;
    background: var(--card-black);
  }
  .brand-name {
    font-family: "Open Sans", sans-serif;
    font-weight: 700;
    font-size: 34px;
    line-height: 1.05;
    text-transform: uppercase;
    color: var(--brand-gold);
  }
</style>
</head>
<body>
<main class="canvas">
  <section class="card card-contact" aria-label="Contact side">
    <div class="contact-block">
      <p class="person-name">Ned Paxley</p>
      <p class="person-title">Director</p>
      <ul class="contact-list">
        <li class="contact-item">
          <svg class="contact-icon" viewBox="0 0 16 16" aria-hidden="true"><circle cx="8" cy="8" r="8" fill="#f4f4f4"/><path d="M5 4.5l1.6-.5 1 2.2-1 .8a5 5 0 0 0 2.4 2.4l.8-1 2.2 1-.5 1.6c-3.5 0-6.5-3-6.5-6.5z" fill="#050505"/></svg>
          1300 472 861
        </li>
        <li class="contact-item">
          <svg class="contact-icon" viewBox="0 0 16 16" aria-hidden="true"><circle cx="8" cy="8" r="8" fill="#f4f4f4"/><rect x="5.5" y="3.5" width="5" height="9" rx="1" fill="#050505"/></svg>
          0438 705 705
        </li>
        <li class="contact-item">
          <svg class="contact-icon" viewBox="0 0 16 16" aria-hidden="true"><circle cx="8" cy="8" r="8" fill="#f4f4f4"/><rect x="4" y="5" width="8" height="6" fill="#050505"/><path d="M4 5l4 3 4-3" stroke="#f4f4f4" fill="none"/></svg>
          info@rubydeckfun.com.au
        </li>
        <li class="contact-item">
          <svg class="contact-icon" viewBox="0 0 16 16" aria-hidden="true"><circle cx="8" cy="8" r="8" fill="#f4f4f4"/><circle cx="8" cy="8" r="4" fill="none" stroke="#050505"/><path d="M4 8h8M8 4v8" stroke="#050505"/></svg>
          www.rubydeckfun.com.au
        </li>
        <li class="contact-item">
          <span class="contact-icon-pair" aria-hidden="true">
            <svg class="contact-icon" viewBox="0 0 16 16"><circle cx="8" cy="8" r="8" fill="#f4f4f4"/></svg>
            <svg class="contact-icon" viewBox="0 0 16 16"><circle cx="8" cy="8" r="8" fill="#f4f4f4"/></svg>
          </span>
          @rubydeckshowhire
        </li>
      </ul>
    </div>
    <div class="brand-faint" aria-hidden="true">
      <span class="brand-faint-circle"></span>
      <span class="brand-faint-name">Ruby Deck<br>Productions</span>
    </div>
  </section>

  <section class="card card-logo" aria-label="Logo side">
    <div class="bokeh-backdrop" role="img" aria-label="Blurred warm casino lights photograph"></div>
    <div class="brand-mark">
      <span class="brand-circle"></span>
      <span class="brand-name">Ruby Deck<br>Productions</span>
    </div>
  </section>
</main>
</body>
</html>
```